contemporary upscale hair salon

we need a business card design for a modern upscale salon. I would like the card to be vertical, simple, and easy to read. I would like a black matte finish on the info side with white on the back of the card, white lettering with a splash of red incorporated somewhere in there. I also want to incorporate embossing and/or cut out in the letters. The info I would like; Name of the business (Velora Salon) stylist name (Janet) phone number(4075319264) and web address (www.veloraexample.com) I am open to putting shears on the card but without it looking too cheap. Looking for something really modern and edgy. these are just ideas I have, but feel free to show me your creative ideas.
please note: the website is still under construction please do not use any images or colors off the web page. Also i currently do not have a logo, that will be a future project.

```html
<!DOCTYPE html>
<html lang="en">
<head>
<meta charset="utf-8">
<title>Velora Salon – Business Card</title>
<link rel="stylesheet" href="https://fonts.googleapis.com/css2?family=Open+Sans:wght@400&family=Roboto+Condensed:wght@300;400&family=Allura&display=swap">
<style>
  :root {
    --paper: #ffffff;
    --card-dark: #1c2020;
    --red-bright: #f0141e;
    --red-mid: #b8121c;
    --red-deep: #8a1018;
    --red-ring: #561a1e;
    --red-light: #f7a3a3;
    --red-main: #ff4d4d;
    --red-hot: #e0101a;
    --ink: #111111;
    --white: #ffffff;
  }
  * { margin: 0; padding: 0; box-sizing: border-box; }
  html, body {
    width: 1200px; height: 879px;
    overflow: hidden;
    background: var(--paper);
  }
  .sheet { position: relative; width: 1200px; height: 879px; }

  .card { position: absolute; top: 0; height: 879px; overflow: hidden; }
  .card-front { left: 55px; width: 527px; background: var(--card-dark); }
  .card-back { left: 627px; width: 528px; background: var(--paper); }
  .card-shapes { position: absolute; inset: 0; }

  .wordmark {
    position: absolute;
    font-family: "Open Sans", sans-serif;
    font-weight: 400;
    line-height: 1;
    text-align: right;
  }
  .card-front .wordmark {
    top: 26px; right: 26px;
    color: var(--white);
    font-size: 74px;
  }
  .card-back .wordmark {
    top: 140px; left: 150px;
    color: var(--ink);
    font-size: 78px;
  }
  .wordmark span { display: block; }
  .wordmark .second { margin-top: 14px; margin-right: 14px; }

  .stylist {
    position: absolute;
    font-family: "Allura", cursive;
    color: var(--ink);
    line-height: 1;
  }
  .stylist-title { left: 125px; top: 305px; font-size: 58px; }
  .stylist-name { left: 178px; top: 375px; font-size: 92px; }

  .contact {
    position: absolute;
    left: 10px; top: 694px;
    color: var(--white);
  }
  .phone {
    display: flex; align-items: center; gap: 14px;
    font-family: "Roboto Condensed", sans-serif;
    font-weight: 300;
    font-size: 38px;
    letter-spacing: 0.5px;
  }
  .phone svg { width: 20px; height: 34px; }
  .details {
    margin-top: 12px;
    font-family: "Open Sans", sans-serif;
    font-size: 28px;
    line-height: 39px;
  }

  .web {
    position: absolute;
    left: 21px; top: 790px;
    color: var(--white);
    font-family: "Roboto Condensed", sans-serif;
    font-weight: 300;
    font-size: 38px;
  }
</style>
</head>
<body>
<main class="sheet">

  <section class="card card-front" aria-label="Card front">
    <svg class="card-shapes" width="527" height="879" viewBox="0 0 527 879" aria-hidden="true">
      <defs>
        <linearGradient id="redFade" x1="1" y1="0" x2="0.2" y2="0.9">
          <stop offset="0" stop-color="var(--red-bright)"/>
          <stop offset="0.55" stop-color="var(--red-mid)"/>
          <stop offset="1" stop-color="var(--red-deep)"/>
        </linearGradient>
      </defs>
      <circle cx="525" cy="330" r="455" fill="var(--red-ring)"/>
      <circle cx="535" cy="275" r="425" fill="url(#redFade)"/>
    </svg>

    <h1 class="wordmark"><span>Velora</span><span class="second">Salon</span></h1>

    <p class="stylist stylist-title">Stylist</p>
    <p class="stylist stylist-name">Janet</p>

    <div class="contact">
      <p class="phone">
        <svg viewBox="0 0 20 34" aria-hidden="true">
          <path d="M13 2 C6 3 3 9 3 17 C3 25 6 31 13 32 L14 26 C10 25 9 21 9 17 C9 13 10 9 14 8 Z" fill="#d9d9d9"/>
        </svg>
        407-531-9264
      </p>
      <p class="details">info@veloraexample.com<br>1870b North Alder Road<br>Linden, Texas 77012</p>
    </div>
  </section>

  <section class="card card-back" aria-label="Card back">
    <svg class="card-shapes" width="528" height="879" viewBox="0 0 528 879" aria-hidden="true">
      <defs>
        <linearGradient id="redSoftFade" x1="0" y1="0" x2="1" y2="1">
          <stop offset="0" stop-color="var(--red-main)"/>
          <stop offset="0.6" stop-color="var(--red-main)"/>
          <stop offset="1" stop-color="var(--red-hot)"/>
        </linearGradient>
      </defs>
      <circle cx="413" cy="1010" r="605" fill="var(--red-light)"/>
      <circle cx="493" cy="1040" r="620" fill="url(#redSoftFade)"/>
    </svg>

    <h2 class="wordmark"><span>Velora</span><span class="second">Salon</span></h2>

    <p class="web">www.veloraexample.com</p>
  </section>

</main>
</body>
</html>
```